Campaign Flyer for a local election

Black and white election flyer

See information below to be included:

Re-elect Dorian
Experienced Willows Board Member
Experienced NYC Principal
Experienced leader

One Year Board Accomplishments:
-Installed New Park Lights (Bollards)
-Red Brick Road Repair Project
-Established Closer Ties with Our local precinct to frequently monitor the community with directed security patrols. Requested an increased police presence.
-Met with the 62nd Precinct Officials & Assemblywoman, Marla Quintrell to discuss our security issues
- Focused on maintenance of streetlights to make brighter streets
-Negotiated Contract & Hired Our New Landscaper, Oakhollow Landscapers
-Major Homeowner Shrub Replacement Project
- Addressing Standing Water in our Park (Installed French Drain)
- Replaced and upgraded all 5 outdoor circuit breaker panels
-Write monthly community newsletters
-Sewer cleaning project (had all community catch basins cleaned)
-Carefully overseeing our new school project. Coordinating with the sponsor and the school directors
-Delivered a very healthy budget to the community
-Works closely with our committees
-Events: Zoo event, Petting Zoo, Outdoor Movie Night, Egg Hunt

It is my intent to seek re-election.
(Photo) Dorian Lindqvist
-Dedicated to improving our community
-Hard-working…He gets thing done!
-Trustworthy

. .

Please note, I am submitting new information under accomplishments. The list of accomplishments should be in the same sequence, starting with: Met with the 62nd Precinct....
Please carefully review.
----------------------------------------------------------------------------------------------------------------------------------------------------------------

Re-elect Dorian
Experienced NYC Principal
Experienced leader

Last Year’s Board Accomplishments:

-Met with the 62nd Precinct Officials & Assemblywoman, Marla Quintrell, to discuss our security issues. Requested increased police presence.
-Established a strong partnership with the 62nd precinct to frequently monitor the community with directed security patrols.
-Replaced all new park lights (Bollards) to make the park brighter
- Focused on maintenance of streetlights to make streets brighter
-‘Fixing Our Streets Project’ (Repaired all cracked/missing red bricks)
-Homeowner Shrub Replacement Project (Replaced hundreds of bushes)
- I write the monthly community newsletter
-Carefully overseeing our new school project. Coordinating with the sponsor and the school director
-Monitoring C of O’s and homeowners Insurance

(Photo) Dorian Lindqvist
-Hard-working! I get things done!
-Trustworthy

. .

Re-elect Dorian
Experienced NYC Principal
Experienced leader

(Photo) Dorian Lindqvist
-Trustworthy

. .

Target Market(s)

A Community electing a Board Member

Industry/Entity Type

residential election

Requirements
Must have
• all black, white and grey print. Flyers will not be printed in color
Nice to have
• See the information in the attachment below containing all my accomplishments
Should not have
• color

```html
<!DOCTYPE html>
<html lang="en">
<head>
<meta charset="utf-8">
<title>Re-elect Dorian – Campaign Flyer</title>
<link rel="stylesheet" href="https://fonts.googleapis.com/css2?family=Anton&family=Montserrat:wght@500;600;700;800&display=swap">
<style>
  :root{
    --ink:#1c1c1c;
    --band:#6e6e6e;
    --band-dark:#5a5a5a;
    --photo-tone-a:#8a8a8a;
    --photo-tone-b:#3a3a3a;
    --paper:#ffffff;
    --paper-shade:#ececee;
    --backdrop:#dcdcdc;
    --white:#ffffff;
    --tick-grey:#8c8c8c;
  }
  *{box-sizing:border-box;margin:0;padding:0}
  html,body{width:1200px;height:800px;overflow:hidden;background:var(--backdrop)}
  .flyer{
    position:absolute;left:306px;top:20px;width:588px;height:760px;
    background:linear-gradient(180deg,var(--paper) 0%,var(--paper-shade) 100%);
    box-shadow:0 4px 18px rgba(0,0,0,.18);
    overflow:hidden;font-family:"Montserrat",sans-serif;color:var(--ink);
  }
  .photo-panel{
    position:absolute;left:360px;top:0;width:228px;height:300px;
    background:linear-gradient(160deg,var(--photo-tone-a),var(--photo-tone-b));
    clip-path:polygon(0 0,100% 0,100% 100%,30% 100%,0 40%);
  }
  .headline{
    position:absolute;left:26px;top:44px;
    font-family:"Anton",sans-serif;font-size:50px;line-height:1;letter-spacing:.5px;
    text-transform:uppercase;color:var(--ink);white-space:nowrap;
  }
  .credentials{
    position:absolute;left:0;top:112px;width:380px;height:96px;
    background:var(--band);
    clip-path:polygon(0 0,94% 0,100% 50%,94% 100%,0 100%);
    padding:13px 0 0 28px;
  }
  .credentials p{color:var(--white);font-weight:800;font-size:15px;line-height:23px;white-space:nowrap}
  .accomplishments{position:absolute;left:26px;top:220px;width:540px}
  .accomplishments h2{font-size:15px;font-weight:800;margin-bottom:6px}
  .accomplishments ul{list-style:none}
  .accomplishments li{
    position:relative;padding-left:22px;font-size:12px;font-weight:600;line-height:15px;margin-bottom:3px;
  }
  .accomplishments li.beside-photo{max-width:362px}
  .accomplishments li::before{
    content:"";position:absolute;left:2px;top:1.5px;width:12px;height:12px;border-radius:50%;background:var(--tick-grey);
  }
  .accomplishments li::after{
    content:"";position:absolute;left:6px;top:3.5px;width:3px;height:6px;
    border:solid var(--white);border-width:0 2px 2px 0;transform:rotate(45deg);
  }
  .intent-band{
    position:absolute;left:0;top:618px;width:100%;height:42px;background:var(--band);
    display:flex;align-items:center;padding-left:40px;
  }
  .intent-band p{font-family:"Anton",sans-serif;font-size:28px;color:var(--white);letter-spacing:.6px;text-transform:uppercase;white-space:nowrap}
  .candidate-name{
    position:absolute;left:40px;top:670px;font-family:"Anton",sans-serif;font-size:36px;line-height:38px;text-transform:uppercase;
  }
  .qualities{position:absolute;left:226px;top:676px;list-style:none}
  .qualities li{display:flex;align-items:center;gap:8px;font-size:14px;font-weight:800;height:24px;position:relative;white-space:nowrap}
  .qualities li:not(:last-child)::after{
    content:"";position:absolute;left:7px;top:19px;height:10px;border-left:2px dotted var(--band-dark);
  }
  .qualities svg{width:16px;height:16px;flex:none}
</style>
</head>
<body>
  <main class="flyer">
    <div class="photo-panel" role="img" aria-label="Black and white portrait photo of candidate Dorian Lindqvist"></div>

    <h1 class="headline">Re-elect Dorian</h1>

    <div class="credentials">
      <p>Experienced Willows Board Member</p>
      <p>Experienced NYC Principal</p>
      <p>Experienced leader</p>
    </div>

    <section class="accomplishments">
      <h2>One Year Board Accomplishments:</h2>
      <ul>
        <li class="beside-photo">Installed New Park Lights (Bollards)</li>
        <li class="beside-photo">Red Brick Road Repair Project</li>
        <li class="beside-photo">Focused on maintenance of streetlights to make brighter streets</li>
        <li class="beside-photo">Negotiated Contract and Hired Our New Landscaper, Oakhollow Landscapers</li>
        <li>Major Homeowner Shrub Replacement Project</li>
        <li>Replaced and upgraded all 5 outdoor circuit breaker panels</li>
        <li>Write monthly community newsletters</li>
        <li>Addressing Standing Water in our Park (Installed French Drain)</li>
        <li>Sewer cleaning project (had all community catch basins cleaned)</li>
        <li>Established Closer Ties with Our local precinct to frequently monitor the community with directed security patrols. Requested an increased police presence.</li>
        <li>Met with the 62nd Precinct Officials and Assemblywoman, Marla Quintrell to discuss our security issues</li>
        <li>Carefully overseeing our new school project. Coordinating with the sponsor and the school directors</li>
        <li>Delivered a very healthy budget to the community</li>
        <li>Works closely with our committees</li>
        <li>Events: Zoo event, Petting Zoo, Outdoor Movie Night, Egg Hunt</li>
      </ul>
    </section>

    <div class="intent-band"><p>It is my intent to seek re-election</p></div>

    <h2 class="candidate-name">Dorian<br>Lindqvist</h2>

    <ul class="qualities">
      <li><svg viewBox="0 0 16 16"><circle cx="8" cy="8" r="6.5" fill="none" stroke="#5a5a5a" stroke-width="1.5"/><path d="M5 8.2l2 2 4-4.4" fill="none" stroke="#1c1c1c" stroke-width="1.8"/></svg>Dedicated to improving our community</li>
      <li><svg viewBox="0 0 16 16"><circle cx="8" cy="8" r="6.5" fill="none" stroke="#5a5a5a" stroke-width="1.5"/><path d="M5 8.2l2 2 4-4.4" fill="none" stroke="#1c1c1c" stroke-width="1.8"/></svg>Hard-working...He gets thing done!</li>
      <li><svg viewBox="0 0 16 16"><circle cx="8" cy="8" r="6.5" fill="none" stroke="#5a5a5a" stroke-width="1.5"/><path d="M5 8.2l2 2 4-4.4" fill="none" stroke="#1c1c1c" stroke-width="1.8"/></svg>Trustworthy</li>
    </ul>
  </main>
</body>
</html>
```